Modernize and improve usability of our webpage www.lerntausch-brolani.ch (4 languages, mostly static content)

Need to modernize and freshen up the webpages of our association: www.lerntausch-brolani.ch We offer apprenticeship exchanges within Switzerland and abroad. Young people can inform and enroll online. We do the matchmaking with work locations and organize logistics, stay overs etc.
The webpage needs to be in 4 languages (German, French, Italian and English). The main pages will be:
- Landing page: what we do, targeted to our apprentices / young people who enroll for the stages.
- Sup-Page: Registration form for interested apprentices to sign up for the program
- Sub-Page "Company", the firms who would like to send their apprentices on a internship and info on how to join the program
- Sub-Page "Host Family", private people who would be interested in hosting the apprentices (for free) during the stages. Find out about the reqiurements for the host families
- Sub-Page "About Us", who we are, executive team, board of director, our sponsor "Harmil Circle Switzerland"
- Footer: contact (E-Mail, Telephone, WhatsApp), Bank details (IBAN Number), Partnerlogo of Harmil-Circle (see uploaded jpg), Social-Media Links (Facebook, LinkedIn)

Target Market(s)

Young people looking for a "apprenticeship" stage within Switzerland or going from Switzerland abroad

Industry/Entity Type

Apprenticeships: cooks, builders, craftsman, office support, etc.

Number of Pages Required

5+ page

Font styles to use
Other font styles liked:
• Lato (sans serif)

Requirements
Must have
• use colors shown on uploaded PDF-Slides: Make the BLUE the MAIN color, the ORANGE as a secondary color
Nice to have
• Forms using e.g. google forms or survey-monkey forms (external links, no code). Matching & appealing visuals showing young apprentices (can use stock photos)

```html
<!DOCTYPE html>
<html lang="en">
<head>
<meta charset="utf-8">
<title>brolani – Apprenticeship Exchange</title>
<link href="https://fonts.googleapis.com/css2?family=Fira+Sans:wght@400;500;600&family=Arimo:wght@400;700&display=swap" rel="stylesheet">
<style>
:root{
  --navy:#173750;
  --heading:#23486f;
  --orange:#ff6200;
  --light:#f4f4f4;
  --text:#6f6f6f;
  --footer:#262a30;
  --white:#ffffff;
}
*{box-sizing:border-box;margin:0;padding:0}
html,body{width:1200px;height:4641px;overflow:hidden}
body{position:relative;background:var(--light);font-family:"Arimo",Arial,sans-serif;color:var(--text)}
.abs{position:absolute}
.head-font{font-family:"Fira Sans",Arial,sans-serif}
/* header */
.site-header{position:absolute;left:0;top:0;width:1200px;height:79px;background:var(--white)}
.topbar{position:absolute;top:0;right:0;width:790px;height:30px;background:var(--navy);clip-path:polygon(20px 0,100% 0,100% 100%,44px 100%)}
.topbar span{position:absolute;top:9px;font-size:9px;color:#fff}
.topbar .dot{width:8px;height:8px;border-radius:50%;background:#fff;top:11px}
.quote-tab{position:absolute;right:210px;top:0;width:110px;height:30px;background:#223e57;font-size:9px;color:#fff;text-align:center;line-height:30px}
.brand{position:absolute;left:121px;top:34px;font-family:"Fira Sans",sans-serif;font-weight:600;font-size:27px;color:var(--orange)}
.nav{position:absolute;top:50px;left:401px;display:flex;gap:0;font-size:11px;color:#555}
.nav a{position:absolute;white-space:nowrap;color:#555;text-decoration:none}
.nav a.active{color:#222;font-weight:700}
/* hero */
.hero{position:absolute;left:0;top:79px;width:1200px;height:633px;background:linear-gradient(100deg,#2b3137 0%,#4a5157 45%,#7c8286 75%,#5e666c 100%)}
.hero .kicker{left:110px;top:190px;font-size:13px;color:#fff}
.hero .kicker i{display:inline-block;width:42px;height:1px;background:#fff;vertical-align:middle;margin-left:18px}
.hero h1{left:110px;top:245px;font-family:"Fira Sans",sans-serif;font-weight:600;font-size:45px;line-height:57px;color:#fff}
.hero p{left:110px;top:398px;width:410px;font-size:13px;line-height:22px;color:#fff}
.btn{position:absolute;background:var(--orange);color:#fff;font-family:"Fira Sans",sans-serif;font-weight:600;font-size:13px;text-align:center;border-radius:3px}
/* section titles */
.sec-title{position:absolute;left:0;width:1200px;text-align:center;font-family:"Fira Sans",sans-serif;font-weight:600;font-size:31px;color:var(--heading)}
.sec-sub{position:absolute;left:330px;width:540px;text-align:center;font-size:13px;line-height:22px;color:#8a8a8a}
/* feature cards */
.feature{position:absolute;top:971px;width:234px;height:215px;background:#fff;box-shadow:0 2px 8px rgba(0,0,0,.12);text-align:center;border-radius:2px}
.feature svg{position:absolute;left:97px;top:30px}
.feature h3{position:absolute;top:90px;left:0;width:100%;font-family:"Fira Sans",sans-serif;font-weight:600;font-size:19px;line-height:25px;color:var(--heading)}
.feature p{position:absolute;top:145px;left:20px;width:194px;font-size:13px;line-height:22px;color:#8a8a8a}
.feature.dark{background:var(--navy)}
.feature.dark h3,.feature.dark p{color:#fff}
/* empower */
.empower-band{left:281px;top:1321px;width:919px;height:468px;background:var(--navy)}
.empower-photo{left:0;top:1387px;width:582px;height:445px;background:linear-gradient(135deg,#6d8079,#3a4e58 55%,#2a3a55)}
.empower h2{left:632px;top:1412px;font-family:"Fira Sans",sans-serif;font-weight:600;font-size:31px;color:#fff}
.empower p{left:630px;width:430px;font-size:13px;line-height:22px;color:#fff}
/* services */
.service-img{position:absolute;top:2063px;width:320px;height:236px}
.service{position:absolute;top:2240px;width:284px;height:201px;background:#fff;box-shadow:0 2px 8px rgba(0,0,0,.12);padding:22px 38px}
.service h3{font-family:"Fira Sans",sans-serif;font-weight:600;font-size:21px;color:var(--heading);margin-bottom:8px}
.service p{font-size:13px;line-height:22px;color:#8a8a8a}
.service .more{display:block;margin-top:8px;font-size:10px;font-weight:700;color:var(--orange)}
.service.dark{background:var(--navy)}
.service.dark h3,.service.dark p,.service.dark .more{color:#fff}
/* consult */
.consult{left:0;top:2513px;width:1200px;height:294px;background:linear-gradient(90deg,#3b4650,#52606b 50%,#3c4852)}
.consult .phone{top:52px;width:1200px;text-align:center;font-family:"Fira Sans",sans-serif;font-weight:500;font-size:22px;color:#fff}
.consult h2{top:92px;width:1200px;text-align:center;font-family:"Fira Sans",sans-serif;font-weight:600;font-size:32px;color:#fff}
.consult p{top:150px;left:330px;width:540px;text-align:center;font-size:13px;line-height:22px;color:#fff}
.btn-outline{position:absolute;left:520px;top:207px;width:166px;height:44px;border:1px solid #fff;border-radius:3px;color:#fff;font-family:"Fira Sans",sans-serif;font-weight:600;font-size:13px;text-align:center;line-height:42px}
/* reviews */
.review{position:absolute;top:3041px;width:494px;height:254px;background:#efefef}
.review .line{position:absolute;left:63px;top:40px;width:1px;height:175px;background:#666}
.review .qmark{position:absolute;left:38px;top:103px;width:50px;height:50px;border-radius:50%;background:var(--orange);border:3px solid #fff;box-shadow:0 0 0 1px var(--orange)}
.review .stars{position:absolute;left:114px;top:40px;color:var(--orange);font-size:15px;letter-spacing:4px}
.review p{position:absolute;left:114px;top:82px;width:340px;font-size:13px;line-height:22px;color:#777}
.review h4{position:absolute;left:114px;top:172px;font-family:"Fira Sans",sans-serif;font-weight:600;font-size:18px;color:#222}
.review small{position:absolute;left:115px;top:200px;font-size:12px;color:#666}
.review .avatar{position:absolute;left:400px;top:160px;width:60px;height:60px;border-radius:50%;background:linear-gradient(135deg,#d7cfc6,#a79a8d)}
/* contact */
.contact-box{left:88px;top:3596px;width:1018px;height:461px;background:#fff;box-shadow:0 2px 10px rgba(0,0,0,.1)}
.contact-left{left:88px;top:3596px;width:510px;height:461px;background:linear-gradient(135deg,#2b4258,#3a5366 60%,#24384d)}
.cl{position:absolute;color:#fff;font-weight:700}
.field{position:absolute;left:688px;width:332px;background:#f3f3f3;border:1px solid #ececec;font-size:9px;color:#777;padding:8px 14px}
/* orange bar */
.info-bar{left:65px;top:4138px;width:1070px;height:105px;background:var(--orange);border-radius:6px}
.info-bar h5{position:absolute;font-family:"Fira Sans",sans-serif;font-weight:500;font-size:18px;color:#fff}
.info-bar span{position:absolute;font-size:13px;font-weight:700;color:#fff}
/* footer */
.footer{left:0;top:4189px;width:1200px;height:452px;background:var(--footer)}
.footer h4{position:absolute;top:137px;font-family:"Fira Sans",sans-serif;font-weight:600;font-size:18px;color:#fff}
.footer p{position:absolute;font-size:13px;line-height:32px;color:#fff}
.footer a{position:absolute;font-size:13px;color:#fff;text-decoration:underline}
.bottom-strip{left:0;top:4577px;width:1200px;height:64px;border-top:1px solid #3a3e44}
.foot-brand{left:65px;top:4577px;width:171px;height:64px;background:var(--orange);color:#fff;font-family:"Fira Sans",sans-serif;font-weight:600;font-size:27px;text-align:center;line-height:64px}
.social-sq{position:absolute;top:4577px;width:47px;height:64px;border-left:1px solid #3a3e44}
.social-sq i{position:absolute;left:18px;top:27px;width:10px;height:10px;border-radius:50%;background:#555b62}
</style>
</head>
<body>

<header class="site-header">
  <div class="topbar">
    <svg class="abs" style="left:56px;top:9px" width="8" height="11" viewBox="0 0 8 11"><path d="M4 0a4 4 0 0 0-4 4c0 3 4 7 4 7s4-4 4-7a4 4 0 0 0-4-4z" fill="#fff"/><circle cx="4" cy="4" r="1.4" fill="#173750"/></svg>
    <span style="left:68px">8 Alder Lane, Bern 3000</span>
    <span style="left:292px">Follow Us:</span>
    <i class="abs dot" style="left:354px"></i>
    <i class="abs dot" style="left:367px"></i>
    <i class="abs dot" style="left:380px"></i>
  </div>
  <div class="quote-tab">GET QUOTATION</div>
  <div class="brand">brolani</div>
  <nav class="nav">
    <a class="active" style="left:0">Home</a>
    <a style="left:83px">About Us</a>
    <a style="left:164px">Services</a>
    <a style="left:239px">Team</a>
    <a style="left:314px">Gallery</a>
    <a style="left:388px">Solutions</a>
    <a style="left:464px">Contact Us</a>
  </nav>
</header>

<section class="hero" role="img" aria-label="Photo of young people working at computers seen from above">
  <div class="abs kicker">On the other hand<i></i></div>
  <h1 class="abs">Bridging Skills,<br>Connecting Futures</h1>
  <p class="abs">Lorem ipsum dolor sit amet, consectetur adipiscing elit, sed d o eiusmod temp dipiscing elit, sed d</p>
  <div class="btn" style="left:110px;top:478px;width:169px;height:45px;line-height:45px">Contact Us</div>
</section>

<h2 class="sec-title" style="top:841px">Why Choose Us</h2>
<p class="sec-sub" style="top:895px">Lorem ipsum dolor sit amet, consectetur adipiscing elit, sed do eiusmod tempor incididunt ut labore et dolore magna aliqua. Ut enim ad min</p>

<div class="feature" style="left:92px">
  <svg width="40" height="40" viewBox="0 0 40 40" fill="none" stroke="#ff6200" stroke-width="2"><polygon points="20,6 32,14 30,30 10,30 8,14"/><circle cx="20" cy="6" r="3"/><circle cx="32" cy="14" r="3"/><circle cx="8" cy="14" r="3"/></svg>
  <h3>Tailored<br>Solutions</h3>
  <p>Lorem ipsum dolor sit amet, consectetur adipiscing</p>
</div>
<div class="feature dark" style="left:353px">
  <svg width="40" height="40" viewBox="0 0 40 40" fill="none" stroke="#ff6200" stroke-width="2"><path d="M6 34h28M10 34l8-14 6 4 6-12"/><circle cx="20" cy="10" r="4"/></svg>
  <h3>Industry<br>Connections</h3>
  <p>Lorem ipsum dolor sit amet, consectetur adipiscing</p>
</div>
<div class="feature" style="left:612px">
  <svg width="40" height="40" viewBox="0 0 40 40" fill="none" stroke="#ff6200" stroke-width="2"><path d="M6 26a14 14 0 0 1 28 0"/><rect x="5" y="24" width="6" height="10" rx="2"/><rect x="29" y="24" width="6" height="10" rx="2"/></svg>
  <h3>Global<br>Perspective</h3>
  <p>Lorem ipsum dolor sit amet, consectetur adipiscing</p>
</div>
<div class="feature" style="left:872px">
  <svg width="40" height="40" viewBox="0 0 40 40" fill="none" stroke="#ff6200" stroke-width="2"><circle cx="20" cy="13" r="7"/><path d="M7 34c0-7 6-11 13-11s13 4 13 11z"/></svg>
  <h3>Client<br>Centric</h3>
  <p>Lorem ipsum dolor sit amet, consectetur adipiscing</p>
</div>
<div class="btn" style="left:524px;top:1225px;width:166px;height:45px;line-height:45px">Contact Us</div>

<section class="empower">
  <div class="abs empower-band"></div>
  <div class="abs empower-photo" role="img" aria-label="Photo of a smiling young apprentice in a workshop"></div>
  <h2 class="abs">Empower Skills for Growth</h2>
  <p class="abs" style="top:1466px">Lorem ipsum dolor sit amet, consectetur adipiscing elit, sed do eiusmod tempor &nbsp;incididunt ut labore et dolore magna aliqua. Ut e nim ad min veniam, quis nostrud ex.</p>
  <p class="abs" style="top:1541px">Lorem ipsum dolor sit amet, consectetur adipiscing elit, sed do eiusmod tempor &nbsp;incididunt ut labore et dolore magna aliqua. Ut e nim ad min veniam, quis nostrud ex. et dolore magna aliqua. Ut e nim ad min veniam, quis nostrud ex.</p>
  <div class="btn" style="left:631px;top:1652px;width:155px;height:44px;line-height:44px;text-align:left;padding-left:16px">Contact us
    <svg class="abs" style="left:120px;top:16px" width="18" height="12" viewBox="0 0 18 12" fill="none" stroke="#fff" stroke-width="2"><path d="M0 6h16M11 1l5 5-5 5"/></svg>
  </div>
</section>

<h2 class="sec-title" style="top:1910px">Services We Provide</h2>
<p class="sec-sub" style="top:1964px">Lorem ipsum dolor sit amet, consectetur adipiscing elit, sed do eiusmod tempor incididunt ut labore et dolore magna aliqua. Ut enim ad min</p>

<div class="service-img" style="left:94px;background:linear-gradient(135deg,#8a8f6a,#5c6358)" role="img" aria-label="Photo of two apprentices looking at a laptop"></div>
<div class="service-img" style="left:440px;background:linear-gradient(135deg,#4e6b78,#8a6a55)" role="img" aria-label="Photo of colleagues networking at a desk"></div>
<div class="service-img" style="left:786px;background:linear-gradient(135deg,#7b8a63,#a6937a)" role="img" aria-label="Photo of a career guidance meeting"></div>

<div class="service" style="left:112px">
  <h3>Apprentice Matching</h3>
  <p>Lorem ipsum dolor sit amet, cons ectetur adipiscing elit, sed do eiu smod tempor incididunt ut labore et dolore magna aliqua.</p>
  <span class="more">LEARN MORE</span>
</div>
<div class="service dark" style="left:459px">
  <h3>Industry Networking</h3>
  <p>Lorem ipsum dolor sit amet, cons ectetur adipiscing elit, sed do eiu smod tempor incididunt ut labore et dolore magna aliqua.</p>
  <span class="more">LEARN MORE</span>
</div>
<div class="service" style="left:804px">
  <h3>Career Guidance</h3>
  <p>Lorem ipsum dolor sit amet, cons ectetur adipiscing elit, sed do eiu smod tempor incididunt ut labore et dolore magna aliqua.</p>
  <span class="more">LEARN MORE</span>
</div>

<section class="abs consult" role="img" aria-label="Photo of a business meeting in an office, darkened">
  <div class="abs phone">031-555-0142</div>
  <h2 class="abs">Get Free Consultation Today</h2>
  <p class="abs">Lorem ipsum dolor sit amet, consectetur adipiscing elit, sed do eiusmod tempor incididunt ut labore et dolore magna aliqua. Ut enim ad min</p>
  <div class="btn-outline">Contact Us</div>
</section>

<h2 class="sec-title" style="top:2891px">Clients Reviews</h2>
<p class="sec-sub" style="top:2945px">Lorem ipsum dolor sit amet, consectetur adipiscing elit, sed do eiusmod tempor incididunt ut labore et dolore magna aliqua. Ut enim ad min</p>

<div class="review" style="left:90px">
  <div class="line"></div>
  <div class="qmark"><svg width="44" height="44" viewBox="0 0 44 44" fill="#fff"><path d="M13 17h7v7l-3 6h-3l3-6h-4zM24 17h7v7l-3 6h-3l3-6h-4z"/></svg></div>
  <div class="stars">★★★★★</div>
  <p>Lorem ipsum dolor sit amet, consectetur adipiscing elit, sed do eiusmod tempor incididunt ut labore et d olore magna aliqua.</p>
  <h4>Mara Lindqvist</h4>
  <small>Hill Quarter</small>
  <div class="avatar" role="img" aria-label="Portrait photo of the reviewer"></div>
</div>
<div class="review" style="left:609px">
  <div class="line"></div>
  <div class="qmark"><svg width="44" height="44" viewBox="0 0 44 44" fill="#fff"><path d="M13 17h7v7l-3 6h-3l3-6h-4zM24 17h7v7l-3 6h-3l3-6h-4z"/></svg></div>
  <div class="stars">★★★★★</div>
  <p>Lorem ipsum dolor sit amet, consectetur adipiscing elit, sed do eiusmod tempor incididunt ut labore et d olore magna aliqua.</p>
  <h4>Mara Lindqvist</h4>
  <small>Hill Quarter</small>
  <div class="avatar" role="img" aria-label="Portrait photo of the reviewer" style="background:linear-gradient(135deg,#e0c7b0,#b58a6a)"></div>
</div>
<svg class="abs" style="left:563px;top:3338px" width="70" height="12" viewBox="0 0 70 12">
  <circle cx="6" cy="6" r="4" fill="#ff6200"/><circle cx="25" cy="6" r="4" fill="#ff6200"/><circle cx="44" cy="6" r="4" fill="none" stroke="#ff6200" stroke-width="1.5"/><circle cx="63" cy="6" r="4" fill="#ff6200"/>
</svg>

<div class="abs" style="left:0;top:3391px;width:1200px;height:800px;background:#f7f7f7"></div>
<h2 class="sec-title" style="top:3447px">Get in touch with us</h2>
<p class="sec-sub" style="top:3501px">Lorem ipsum dolor sit amet, consectetur adipiscing elit, sed do eiusmod tempor incididunt ut labore et dolore magna aliqua. Ut enim ad min</p>

<div class="abs contact-box"></div>
<div class="abs contact-left" role="img" aria-label="Photo of a man working on a laptop, tinted blue"></div>
<div class="cl" style="left:175px;top:3664px;font-size:17px;font-family:'Fira Sans',sans-serif;font-weight:500">CONTACT US</div>
<div class="cl" style="left:175px;top:3703px;font-size:21px;font-family:'Fira Sans',sans-serif;font-weight:500">Call: 031 555 0199</div>
<div class="cl" style="left:175px;top:3737px;font-size:11px">info@brolani-mail.ch</div>
<div class="cl" style="left:175px;top:3778px;font-size:11px;line-height:17px">Address:<br>ALDER LANE<br>3000 Bern</div>
<div class="cl" style="left:175px;top:3855px;font-size:11px;line-height:17px">Operating Hours<br>Monday to Saturday: 9:00 - 18:00<br>Sunday: Closed</div>
<svg class="abs" style="left:178px;top:3961px" width="160" height="34" viewBox="0 0 160 34">
  <circle cx="17" cy="17" r="15" fill="#6a7885"/><circle cx="58" cy="17" r="15" fill="#fff"/><circle cx="99" cy="17" r="15" fill="#6a7885"/><circle cx="141" cy="17" r="15" fill="#6a7885"/>
</svg>

<div class="abs head-font" style="left:686px;top:3654px;font-size:17px;font-weight:500;color:var(--heading)">FREE CONSULTATION</div>
<div class="field" style="top:3706px;height:32px">Your Name</div>
<div class="field" style="top:3756px;height:31px">Email</div>
<div class="field" style="top:3805px;height:33px">Phone</div>
<div class="field" style="top:3856px;height:93px">Message</div>
<div class="btn" style="left:688px;top:3967px;width:110px;height:36px;line-height:36px;font-size:11px">SUBMIT</div>

<section class="abs footer">
  <h4 style="left:67px">About Company</h4>
  <p style="left:67px;top:200px;width:310px">Lorem ipsum dolor sit amet, consectetur adipis cing elit, sed do eiusmod tempor incididunt ut labore et dolore magna aliqua.</p>
  <a style="left:67px;top:305px;color:#3aa0e8;font-size:15px">Read More</a>
  <h4 style="left:434px">Useful Links</h4>
  <a style="left:434px;top:208px">About Us</a>
  <a style="left:434px;top:240px">Projects</a>
  <a style="left:434px;top:274px">Blog</a>
  <a style="left:434px;top:306px">Contact Us</a>
  <a style="left:611px;top:208px">Services</a>
  <a style="left:611px;top:240px">Shop</a>
  <a style="left:611px;top:274px">Privacy Policy</a>
  <a style="left:611px;top:306px">Help Desk</a>
  <h4 style="left:798px">Subscribe</h4>
  <p style="left:798px;top:200px;width:340px;line-height:25px;font-size:14px">If you have any questions, Subscribe to our newsleteer to know more</p>
  <div class="abs" style="left:796px;top:258px;width:339px;height:52px;background:#fff;border-radius:3px">
    <span class="abs" style="left:16px;top:19px;font-size:12px;color:#777">Email</span>
    <div class="abs" style="right:0;top:0;width:63px;height:52px;background:var(--orange);border-radius:0 3px 3px 0">
      <svg class="abs" style="left:24px;top:17px" width="14" height="18" viewBox="0 0 14 18" fill="none" stroke="#fff" stroke-width="3"><path d="M3 2l8 7-8 7"/></svg>
    </div>
  </div>
</section>

<div class="abs info-bar">
  <svg class="abs" style="left:40px;top:30px" width="52" height="46" viewBox="0 0 52 46" fill="none" stroke="#fff" stroke-width="2"><path d="M26 4a10 10 0 0 0-10 10c0 8 10 18 10 18s10-10 10-18A10 10 0 0 0 26 4z"/><circle cx="26" cy="14" r="4"/><path d="M14 30l-10 12h44l-10-12"/></svg>
  <h5 style="left:110px;top:28px">Address</h5>
  <span style="left:110px;top:60px">8, Bern, Switzerland</span>
  <svg class="abs" style="left:348px;top:0" width="22" height="105" viewBox="0 0 22 105" fill="none" stroke="#fff" stroke-width="2"><path d="M2 0l18 52L2 105"/></svg>
  <svg class="abs" style="left:405px;top:28px" width="44" height="52" viewBox="0 0 44 52" fill="none" stroke="#fff" stroke-width="2"><rect x="4" y="2" width="22" height="46" rx="3"/><path d="M4 38h22M13 43h4M32 16a8 8 0 0 1 0 14M36 11a14 14 0 0 1 0 24"/></svg>
  <h5 style="left:466px;top:28px">Phone</h5>
  <span style="left:466px;top:60px">+41 31 555 0177</span>
  <svg class="abs" style="left:706px;top:0" width="22" height="105" viewBox="0 0 22 105" fill="none" stroke="#fff" stroke-width="2"><path d="M2 0l18 52L2 105"/></svg>
  <svg class="abs" style="left:755px;top:30px" width="50" height="46" viewBox="0 0 50 46" fill="none" stroke="#fff" stroke-width="2"><path d="M4 16l21-13 21 13v26H4z"/><path d="M4 16l21 14 21-14"/><path d="M11 12h28v10"/></svg>
  <h5 style="left:824px;top:28px">Email Contact</h5>
  <span style="left:824px;top:60px">info@brolani-mail.ch</span>
</div>

<div class="abs bottom-strip"></div>
<div class="abs foot-brand">brolani</div>
<div class="social-sq" style="left:905px"><i></i></div>
<div class="social-sq" style="left:952px"><i></i></div>
<div class="social-sq" style="left:999px"><i></i></div>
<div class="social-sq" style="left:1046px"><i></i></div>
<div class="social-sq" style="left:1093px;width:42px;border-right:1px solid #3a3e44"><i style="left:16px"></i></div>

</body>
</html>
```